Morvaleth Company Notepad / Grid pad / Graph pad

I need a "modern" version of this graph pad. The information at the top needs to be shown, along with the graph lines, however, I need this more "interesting" than it currently is. This will be printed and bound at the TOP edge with 50 sheets per pack.

Target Market(s)

Clients - Want to show sophistication and not childish.

Industry/Entity Type

Structural Engineering

Font styles to use
Sans Serif

Colors
0255a3
85abd2

Requirements
Must have
• My project must have all of the elements currently shown on the pdf
Should not have
• My project should not have clipart images.

```html
<!DOCTYPE html>
<html lang="en">
<head>
<meta charset="utf-8">
<title>Morvaleth Company Grid Pad</title>
<link rel="stylesheet" href="https://fonts.googleapis.com/css2?family=Open+Sans:wght@400;600;700&display=swap">
<style>
  :root {
    --brand-blue: #1f5276;
    --accent-gray: #7d8186;
    --paper: #f5f4f2;
    --field-fill: #dcdcdc;
    --grid-line: #bdbdbd;
    --grid-frame: #6b6b6b;
    --ink: #1c1c1c;
  }
  * { box-sizing: border-box; margin: 0; padding: 0; }
  html, body { width: 956px; height: 1200px; overflow: hidden; }
  body {
    background: var(--paper);
    font-family: "Open Sans", sans-serif;
    color: var(--ink);
  }
  .sheet { position: relative; width: 956px; height: 1200px; background: var(--paper); }
  .header-band { position: absolute; left: 0; top: 0; width: 956px; height: 130px; }

  .brand { position: absolute; left: 70px; top: 102px; width: 270px; text-align: center; }
  .brand-name {
    font-weight: 700; font-size: 27px; line-height: 31px;
    color: var(--brand-blue); letter-spacing: 0.5px;
  }

  .field-label {
    position: absolute; width: 80px; text-align: right;
    font-size: 14px; font-weight: 700; color: var(--brand-blue); line-height: 24px;
  }
  .field-box { position: absolute; height: 24px; background: var(--field-fill); }
  .field-of { position: absolute; left: 548px; width: 20px; text-align: center; font-size: 13px; font-weight: 700; line-height: 24px; }

  .grid-area {
    position: absolute; left: 23px; top: 188px; width: 911px; height: 961px;
    border: 1.5px solid var(--grid-frame);
    background-image:
      linear-gradient(to right, var(--grid-line) 1px, transparent 1px),
      linear-gradient(to bottom, var(--grid-line) 1px, transparent 1px);
    background-size: calc(100% / 32) calc(100% / 46);
  }

  .contact-line {
    position: absolute; left: 0; top: 1162px; width: 956px;
    display: flex; justify-content: center; align-items: center; gap: 8px;
    font-size: 14px; line-height: 20px; color: var(--ink);
  }
  .contact-item { display: flex; align-items: center; gap: 5px; white-space: nowrap; }
  .contact-item + .contact-item { margin-left: 6px; }
  .contact-icon { width: 12px; height: 13px; fill: var(--brand-blue); }
</style>
</head>
<body>
<main class="sheet">
  <svg class="header-band" viewBox="0 0 956 130" aria-hidden="true">
    <path d="M0,49 Q346,15 647,23 Q900,36 956,116 L956,130 Q900,44 647,27 Q346,19 0,52 Z" fill="var(--accent-gray)"/>
    <path d="M0,0 H956 V113 Q900,36 647,23 Q346,15 0,49 Z" fill="var(--brand-blue)"/>
  </svg>

  <div class="brand">
    <div class="brand-name">MORVALETH<br>COMPANY</div>
  </div>

  <div class="field-label" style="left:383px; top:87px;">Project</div>
  <div class="field-box" style="left:473px; top:87px; width:174px;"></div>
  <div class="field-label" style="left:630px; top:87px;">Job No</div>
  <div class="field-box" style="left:720px; top:87px; width:174px;"></div>

  <div class="field-label" style="left:383px; top:115px;">Task</div>
  <div class="field-box" style="left:473px; top:115px; width:174px;"></div>
  <div class="field-label" style="left:630px; top:115px;">Author</div>
  <div class="field-box" style="left:720px; top:115px; width:174px;"></div>

  <div class="field-label" style="left:383px; top:145px;">Page</div>
  <div class="field-box" style="left:473px; top:146px; width:62px;"></div>
  <div class="field-of" style="top:146px;">of</div>
  <div class="field-box" style="left:585px; top:146px; width:62px;"></div>
  <div class="field-label" style="left:630px; top:145px;">Date</div>
  <div class="field-box" style="left:720px; top:146px; width:174px;"></div>

  <div class="grid-area"></div>

  <footer class="contact-line">
    <span class="contact-item">
      <svg class="contact-icon" viewBox="0 0 12 16"><path d="M6 0a6 6 0 0 0-6 6c0 4.5 6 10 6 10s6-5.5 6-10a6 6 0 0 0-6-6zm0 8.5A2.5 2.5 0 1 1 6 3.5a2.5 2.5 0 0 1 0 5z"/></svg>
      215 Coral Ridge Avenue, Suite 204, Lake Worth, FL 33460
    </span>
    <span class="contact-item">
      <svg class="contact-icon" viewBox="0 0 16 16"><path d="M3.6 1 6 3.6 4.6 5.4a9 9 0 0 0 6 6L12.4 10 15 12.4 13.4 15C6.8 15 1 9.2 1 2.6z"/></svg>
      561.555.0147
    </span>
    <span class="contact-item">
      <svg class="contact-icon" viewBox="0 0 16 16"><circle cx="8" cy="8" r="7"/><path d="M4 6h4v3H6zM9 10h3v2H9z" fill="var(--paper)"/></svg>
      www.morvalethcompany.com
    </span>
  </footer>
</main>
</body>
</html>
```